Logo+Business Card Design for Architecture Photographer

Hi Everyone,

I am looking for logo/business designs for my new business - Brovald Studio. My business does commercial photography with a specialization in architecture, luxury real estate, and design. The Int is short for interior and ex is short for exterior.

Some of the values of my business are:
- providing top quality photography and post-processing (straight lines, accurate and bold whites/blacks/colors) for commercial use (websites, social media, advertising campaigns)
- fostering a collaborative workflow that is professional and fun that will have clients returning because of the premium service they received
- asking the right questions so that I can capture what matters to my clients with my own creative vision

I want my final look to be modern and bold. The business cards will be letter pressed/debossed, so the design should incorporate that. I am imagining a solid matte olive green or matte navy blue background on one side and white on the other. The card will be printed on colored cards, so you don't have to put a colored background as part of the design. I have attached some examples of colors I like, although it doesn't matter too much for the purpose of your work.

I want the debossing to be part of the design of the business card. This debossing should be some some of pattern or a frame that holds the logo on the back of the card (I have attached some sample images named geometric debossing to show what I mean). Then I can just foil print my logo on the back. My contact info and a logo will be on the front.

Somewhere it should say "Architecture, Luxury Real Estate, Design".

My vision for the logo: no cameras or buildings. I can't think of anything symbolic for the logo, but it should somehow contain Brovald. It might be cool to have them separated by a line like Bro | Vald. Or have the Int inside something, and the Ex outside.

I plan on using Quelmark to print the cards. You can find their specifications here: https://quelmark.example/products/duplex-business-cards?variant=4837201956372

It would be nice to have a psd file that I can edit as well as a PDF to deliver to the printing company. Both must be vector graphics.

Thank you to everyone who has submitted a design as it has helped me get a better idea of what I want.

Target Market(s)

Designers, architects

Industry/Entity Type

Photographer

Contact Information for Business Card

See project description

Logo Text

Brovald Studio

Font styles to use
Sans Serif
Decorative

Colors
ffffff

Requirements
Must have
• Logo and business card design. Deboss area less than 3 square inches. Deboss area should be some sort of a pattern/design as shown in attachments labelled "Geometric Debossing Example".
• Logo design and deboss design must be submitted in vector graphics.
Nice to have
• Color doesn't have to be shown on the design because I will be printing on colored paper, although it would be helpful to help me visualize what it will eventually look like.
Should not have
• A camera or building in the design...too cliche.

```html
<!DOCTYPE html>
<html lang="en">
<head>
<meta charset="utf-8">
<title>Brovald Studio – Business Card</title>
<link rel="stylesheet" href="https://fonts.googleapis.com/css2?family=Cormorant+Garamond:wght@500&display=swap">
<style>
  :root {
    --card-green: #1b2f1b;
    --card-shadow: #14211a;
    --frame-line: #9aa596;
    --ink-white: #ffffff;
    --ink-sage: #d3e6cc;
    --page: #ffffff;
  }
  html, body {
    margin: 0;
    padding: 0;
    width: 981px;
    height: 1200px;
    overflow: hidden;
    background: var(--page);
  }
  .card-sheet {
    display: block;
    width: 981px;
    height: 1200px;
  }
  .card-sheet text {
    font-family: "Cormorant Garamond", Georgia, serif;
    font-weight: 500;
    font-variant-numeric: lining-nums;
  }
  .bg-green { fill: var(--card-green); }
  .bg-shadow { fill: var(--card-shadow); }
  .deboss-frame { fill: none; stroke: var(--frame-line); stroke-width: 1.2; }
  .wordmark { fill: var(--ink-white); letter-spacing: 2px; }
  .tagline { fill: var(--ink-sage); }
  .contact-name { fill: var(--ink-sage); }
  .contact-line { fill: var(--ink-white); }
</style>
</head>
<body>
<svg class="card-sheet" viewBox="0 0 1050 1284" xmlns="http://www.w3.org/2000/svg">
  <g class="card-back">
    <rect class="bg-green" x="0" y="0" width="1050" height="600"/>
    <polygon class="bg-shadow" points="320,213 795,213 605,600 18,600"/>
    <rect class="deboss-frame" x="33" y="33" width="984" height="534"/>
    <text class="wordmark" x="553" y="326" font-size="90" text-anchor="middle">BROVALD</text>
    <text class="tagline" x="558" y="406" font-size="28" text-anchor="middle">Architecture, Luxury Real Estate, Design</text>
  </g>

  <g class="card-front" transform="translate(0 683)">
    <rect class="bg-green" x="0" y="0" width="1050" height="601"/>
    <polygon class="bg-shadow" points="775,0 1050,0 1050,601 310,601"/>
    <polygon class="bg-shadow" points="145,110 458,110 140,601 0,601 0,292"/>
    <rect class="deboss-frame" x="33" y="34" width="984" height="533"/>

    <text class="wordmark" x="300" y="188" font-size="60" text-anchor="middle">BROVALD</text>
    <text class="tagline" x="302" y="247" font-size="26" text-anchor="middle">Architecture Photographer</text>

    <text class="contact-name" x="586" y="174" font-size="37">Mara Ellison</text>
    <text class="contact-line" x="586" y="240" font-size="37">T: 800-555-0142</text>
    <text class="contact-line" x="586" y="307" font-size="37">studio@brovald.example</text>
    <text class="contact-line" x="586" y="374" font-size="37">www.brovald.example</text>
    <text class="contact-line" x="586" y="440" font-size="37">218 Larkmoor Road East</text>
    <text class="contact-line" x="586" y="473" font-size="37">Fenwick, IN</text>
  </g>
</svg>
</body>
</html>
```